Celling poster

It is a celling poster with questions that you ask yourself in the morning and a morning prayer + evening questions. People might put it on celling or on the wall.

Here is the contant, it is in Slovenian, but I have send you translation.

PO JUTRU SE DAN POZNA ...

1. Kaj me trenutno najbolj veseli v življenju?
3. Na kaj sem ponosna v življenju?
4. Za katere stvari danes čutim največ hvaležnosti?
5. V čem trenutno najbolj uživam?
6. Koga imam rada in kdo me ima rad?

Danes vstajam
s pomočjo nebeških sil:
svetlobe sonca,
sija lune,
žara ognja,
hitrosti strele,
okretnosti vetra,
globine morja,
stanovitnosti zemlje,
trdnosti skale.

VEČERNE MODROSTI

1. Kaj je bil danes moj prispevek svetu?
2. Kaj sem se danes naučila?
3. Katera situacija v dnevu mi je prinesla največ občutkov topline?

TRANSLATION for your understanding.

MORNING POWER QUESTIONS
1. What am I happy abou in my life right now?
2. What am I excited about in my life now?
3. What am I proud about in my life now?
4. What am I grateful about in my life now?
5. What am I enjoying most in my life now?
6. Who do I love? Who loves me?

MORNING PRAYER
Today I am waking up with the power of heavenly forces.
With the light of sun,
light of moon,
light of fire,
speed of lightning,
flexibility of wind,
depps of ocean,
stability of earth and
hardness of rock.

EVENING QUESTIONS OF WISDOM
1. What have I given today?
2. What did I learn today?
3. Which situations today gave me the most feelings of love, warmth?

```html
<!DOCTYPE html>
<html lang="sl">
<head>
<meta charset="utf-8">
<title>Po jutru se dan pozna – plakat</title>
<link rel="stylesheet" href="https://fonts.googleapis.com/css2?family=Federo&family=Dancing+Script:wght@400;700&family=Roboto:wght@500;700&display=swap">
<style>
  :root {
    --page-bg: #e9e6e1;
    --sky-orange: #f26b21;
    --sky-amber: #f7a11b;
    --sky-yellow: #ffd400;
    --sky-pale: #fff2b0;
    --mist-blue: #6cb0d6;
    --mist-white: #d9eaf2;
    --deep-blue: #2b6a9c;
    --night: #0b1030;
    --ink: #0d0f2a;
    --white: #ffffff;
    --frame-dark: #141633;
    --frame-light: #c9ccd8;
    --sun-glow: rgba(255, 250, 215, 0.5);
    --bubble-orange: #f7a23a;
    --bubble-yellow: #f8c033;
  }
  html, body {
    margin: 0;
    width: 1200px;
    height: 1200px;
    overflow: hidden;
    background: var(--page-bg);
  }
  .poster {
    position: absolute;
    left: 180px;
    top: 40px;
    width: 840px;
    height: 1120px;
    overflow: hidden;
  }
  .poster__sky {
    position: absolute;
    inset: 0;
    background: linear-gradient(to bottom,
      var(--sky-orange) 0%,
      var(--sky-amber) 26%,
      var(--sky-yellow) 44%,
      var(--sky-pale) 58%,
      var(--mist-blue) 66%,
      var(--mist-white) 71%,
      var(--mist-blue) 76%,
      var(--deep-blue) 82%,
      var(--night) 92%,
      var(--night) 100%);
  }
  .poster__frame {
    position: absolute;
    left: 23px;
    top: 24px;
    width: 789px;
    height: 1061px;
    border: 4px solid var(--frame-dark);
    box-shadow: inset 0 0 0 2px var(--frame-light);
  }
  .sun {
    position: absolute;
    left: 254px;
    top: 380px;
    width: 318px;
    height: 318px;
    border-radius: 50%;
    background: var(--sun-glow);
  }
  .title {
    position: absolute;
    margin: 0;
    font-family: "Federo", sans-serif;
    font-weight: 400;
    white-space: nowrap;
  }
  .title--morning {
    left: 70px;
    top: 66px;
    font-size: 50px;
    color: var(--ink);
    -webkit-text-stroke: 1.4px var(--ink);
  }
  .title--rise {
    left: 0;
    width: 840px;
    top: 310px;
    text-align: center;
    font-size: 70px;
    color: var(--ink);
    -webkit-text-stroke: 1.6px var(--ink);
  }
  .title--evening {
    left: 67px;
    top: 866px;
    font-size: 50px;
    color: var(--white);
    -webkit-text-stroke: 1.4px var(--white);
  }
  .questions {
    position: absolute;
    margin: 0;
    padding: 0;
    list-style: none;
    font-family: "Roboto", sans-serif;
    white-space: nowrap;
  }
  .questions--morning {
    left: 71px;
    top: 124px;
    font-size: 23px;
    font-weight: 700;
    line-height: 27.7px;
    color: var(--ink);
  }
  .questions--evening {
    left: 67px;
    top: 942px;
    font-size: 23.5px;
    font-weight: 500;
    line-height: 37.5px;
    color: var(--white);
  }
  .prayer {
    position: absolute;
    left: 0;
    top: 404px;
    width: 840px;
    margin: 0;
    text-align: center;
    font-family: "Dancing Script", cursive;
    color: var(--ink);
  }
  .prayer__lead {
    display: block;
    font-size: 43px;
    font-weight: 700;
    line-height: 46px;
  }
  .prayer__line {
    display: block;
    font-size: 34px;
    font-weight: 400;
    line-height: 39.6px;
  }
  .prayer__lead + .prayer__line { margin-top: 2px; }
  .bubbles {
    position: absolute;
    left: 590px;
    top: 880px;
    width: 146px;
    height: 118px;
    border-radius: 50%;
    background: radial-gradient(ellipse at 40% 55%, var(--bubble-orange) 0%, var(--bubble-yellow) 70%);
  }
</style>
</head>
<body>
  <main class="poster">
    <div class="poster__sky" role="img" aria-label="Sončni vzhod nad zasneženimi gorami v meglicah, ki se spušča v nočno modro nebo"></div>
    <div class="sun"></div>
    <div class="poster__frame"></div>

    <h1 class="title title--morning">PO JUTRU SE DAN POZNA ...</h1>
    <ol class="questions questions--morning">
      <li>1. Kaj me trenutno najbolj veseli v življenju?</li>
      <li>3. Na kaj sem ponosna v življenju?</li>
      <li>4. Za katere stvari danes čutim največ hvaležnosti?</li>
      <li>5. V čem trenutno najbolj uživam?</li>
      <li>6. Koga imam rada in kdo me ima rad?</li>
    </ol>

    <h2 class="title title--rise">Danes vstajam</h2>
    <p class="prayer">
      <span class="prayer__lead">s pomočjo</span>
      <span class="prayer__lead">nebeških sil:</span>
      <span class="prayer__line">svetlobe sonca,</span>
      <span class="prayer__line">sija lune,</span>
      <span class="prayer__line">žara ognja,</span>
      <span class="prayer__line">hitrosti strele,</span>
      <span class="prayer__line">okretnosti vetra,</span>
      <span class="prayer__line">globine morja,</span>
      <span class="prayer__line">stanovitnosti zemlje,</span>
      <span class="prayer__line">trdnosti skale.</span>
    </p>

    <h2 class="title title--evening">VEČERNE MODROSTI</h2>
    <div class="bubbles" role="img" aria-label="Skupina oranžnih in rumenih oblačkov z vprašaji"></div>
    <ol class="questions questions--evening">
      <li>1. Kaj je bil danes moj prispevek svetu?</li>
      <li>2. Kaj sem se danes naučila?</li>
      <li>3. Katera situacija v dnevu mi je prinesla največ občutkov topline?</li>
    </ol>
  </main>
</body>
</html>
```